Halvik Partners Building Business Cards

We need a business card that reflects our business as "Solar Experts" in San Diego. Browse our website www.halvikpartners.example our License needs to be displayed as "CSLB# 4871306" our phone number is (619) 482-5537

Save thousands on your electric bills and increase the value of your home while helping to protect the environment. Our solar installation experts will help you design the system that's right for you, using only the highest quality equipment that will look great and give you ideal performance. Our goal is to make you energy independent, and get your electric bill to 0.

Paul Ostrander
(619) 482-5537
paul@halvikpartners.example

Target Market(s)

Home owners in san diego looking for solar

Industry/Entity Type

Solar Energy

Contact Information for Business Card

Paul Ostrander
(619) 482-5537
paul@halvikpartners.example

Font styles to use
Other font styles liked:
• Use our logo font

Requirements
Must have
• License needs to be displayed as "CSLB# 4871306" our phone number is (619) 482-5537
Nice to have
• Real images of rooftop home solar in san diego
Should not have
• our business address

```html
<!DOCTYPE html>
<html lang="en">
<head>
<meta charset="utf-8">
<title>Halvik Partners Building – Business Cards</title>
<link rel="stylesheet" href="https://fonts.googleapis.com/css2?family=Roboto:wght@400;500;700&display=swap">
<style>
  :root {
    --stage: #a7a4a4;
    --navy: #2b4a94;
    --navy-deep: #233f86;
    --sun: #f0a915;
    --paper: #fbfbfa;
    --ink: #233f86;
    --muted: #e6e6e6;
  }
  * { box-sizing: border-box; margin: 0; padding: 0; }
  html, body { width: 1200px; height: 1200px; overflow: hidden; }
  body {
    background: var(--stage);
    font-family: "Roboto", Arial, sans-serif;
    position: relative;
  }
  .card {
    position: absolute;
    border-radius: 24px;
    overflow: hidden;
  }

  /* Front */
  .card-front {
    left: 238px; top: 118px; width: 712px; height: 419px;
    background: var(--navy);
  }
  .front-backdrop {
    position: absolute; inset: 0;
    background: linear-gradient(160deg, #30509b 0%, #2a4890 55%, #27448a 100%);
  }
  .front-name {
    position: absolute; left: 0; right: 0; top: 52px;
    text-align: center; color: #fff;
    font-weight: 700; font-size: 50px; letter-spacing: -0.5px;
  }
  .process-title {
    position: absolute; left: 0; right: 0; top: 205px;
    display: flex; justify-content: center; align-items: center; gap: 26px;
    color: #fff; font-weight: 500; font-size: 23px; letter-spacing: 4px;
  }
  .process-title::before, .process-title::after {
    content: ""; width: 54px; height: 3px; background: var(--sun);
  }
  .process-steps { position: absolute; left: 0; top: 252px; width: 712px; height: 140px; }
  .step-box {
    position: absolute; top: 0; width: 78px; height: 78px;
    background: var(--sun);
    display: flex; align-items: center; justify-content: center;
  }
  .step-label {
    position: absolute; top: 86px; width: 140px;
    text-align: center; color: #fff; font-size: 13.5px; line-height: 15px;
  }
  .step-link {
    position: absolute; top: 38px; height: 0;
    border-top: 2px dotted #fff;
  }

  /* Back */
  .card-back {
    left: 231px; top: 645px; width: 711px; height: 415px;
    background: var(--paper);
  }
  .back-accent {
    position: absolute; right: -60px; top: 40px;
    width: 300px; height: 300px; border-radius: 50%;
    background: #efefef;
  }
  .back-brand {
    position: absolute; left: 50px; top: 140px; width: 250px;
    display: flex; flex-direction: column; align-items: center; gap: 14px;
  }
  .back-brand-dot { width: 64px; height: 64px; border-radius: 50%; background: var(--sun); }
  .back-brand-name {
    color: var(--ink); font-weight: 700; font-size: 25px; line-height: 29px; text-align: center;
  }
  .back-divider {
    position: absolute; left: 336px; top: 80px; width: 1px; height: 210px; background: #e2e2e2;
  }
  .holder-name {
    position: absolute; left: 400px; top: 104px;
    color: var(--ink); font-weight: 700; font-size: 26px;
  }
  .holder-role {
    position: absolute; left: 401px; top: 138px;
    color: var(--ink); font-size: 17px;
  }
  .contact-list { position: absolute; left: 400px; top: 188px; list-style: none; }
  .contact-list li {
    display: flex; align-items: center; gap: 16px;
    height: 25px; color: var(--ink); font-size: 18px;
  }
  .contact-list svg { width: 20px; height: 18px; flex: none; }
  .web-highlight { color: var(--sun); }
  .back-bands { position: absolute; left: 0; bottom: 0; width: 711px; height: 52px; }
  .license {
    position: absolute; left: 400px; top: 377px;
    color: #fff; font-size: 18px;
  }
</style>
</head>
<body>

<section class="card card-front">
  <div class="front-backdrop" role="img" aria-label="Faint photo of rooftop solar panels"></div>
  <div class="front-name">Halvik Partners Building</div>
  <div class="process-title">OUR PROCESS</div>

  <div class="process-steps">
    <span class="step-link" style="left:170px;width:72px"></span>
    <span class="step-link" style="left:320px;width:72px"></span>
    <span class="step-link" style="left:470px;width:73px"></span>

    <div class="step-box" style="left:92px">
      <svg width="40" height="40" viewBox="0 0 40 40" fill="none" stroke="#233f86" stroke-width="3.5">
        <circle cx="16" cy="16" r="10"/><line x1="23" y1="23" x2="34" y2="34" stroke-width="6" stroke-linecap="round"/>
      </svg>
    </div>
    <div class="step-label" style="left:61px">Site<br>Evaluation</div>

    <div class="step-box" style="left:242px">
      <svg width="40" height="40" viewBox="0 0 40 40" fill="none" stroke="#233f86" stroke-width="3" stroke-linejoin="round">
        <path d="M8 6 L34 30 L36 36 L30 34 L4 10 Z"/><line x1="28" y1="24" x2="24" y2="28"/>
      </svg>
    </div>
    <div class="step-label" style="left:211px">Design &amp;<br>Permitting</div>

    <div class="step-box" style="left:392px">
      <svg width="42" height="40" viewBox="0 0 42 40">
        <rect x="8" y="6" width="30" height="20" rx="2" fill="#233f86" transform="rotate(-12 23 16)"/>
        <rect x="4" y="14" width="32" height="21" rx="2" fill="#233f86" stroke="#f0a915" stroke-width="1.5"/>
        <rect x="4" y="19" width="32" height="4" fill="#f0a915"/>
      </svg>
    </div>
    <div class="step-label" style="left:361px">Purchase of<br>Materials</div>

    <div class="step-box" style="left:543px">
      <svg width="44" height="44" viewBox="0 0 44 44" fill="none" stroke="#233f86" stroke-linecap="round">
        <line x1="8" y1="36" x2="30" y2="14" stroke-width="5"/>
        <circle cx="33" cy="11" r="6" stroke-width="3.5"/>
        <line x1="10" y1="8" x2="36" y2="36" stroke-width="4"/>
        <line x1="6" y1="6" x2="12" y2="12" stroke-width="6"/>
      </svg>
    </div>
    <div class="step-label" style="left:512px">Installation &amp;<br>Commissioning</div>
  </div>
</section>

<section class="card card-back">
  <div class="back-accent"></div>
  <div class="back-brand">
    <span class="back-brand-dot"></span>
    <span class="back-brand-name">Halvik Partners<br>Building</span>
  </div>
  <div class="back-divider"></div>

  <div class="holder-name">Paul Ostrander</div>
  <div class="holder-role">Managing Director</div>

  <ul class="contact-list">
    <li>
      <svg viewBox="0 0 20 18"><path d="M2 6 Q10 0 18 6 L16 8 L13 6 L13 4 Q10 3 7 4 L7 6 L4 8 Z M5 9 L15 9 L17 16 L3 16 Z" fill="#f0a915"/></svg>
      (619) 482-5537
    </li>
    <li>
      <svg viewBox="0 0 20 18" fill="none" stroke="#f0a915" stroke-width="1.6"><circle cx="10" cy="9" r="7"/><ellipse cx="10" cy="9" rx="3" ry="7"/><line x1="3" y1="9" x2="17" y2="9"/></svg>
      paul@halvikpartners.example
    </li>
    <li>
      <svg viewBox="0 0 20 18"><rect x="1" y="3" width="18" height="12" fill="#f0a915"/><path d="M1 3 L10 10 L19 3" fill="none" stroke="#fff" stroke-width="1.5"/></svg>
      <span>www.<span class="web-highlight">halvikpartners</span>.example</span>
    </li>
  </ul>

  <svg class="back-bands" viewBox="0 0 711 52" preserveAspectRatio="none">
    <rect x="0" y="25" width="360" height="27" fill="#f0a915"/>
    <polygon points="365,0 711,0 711,52 335,52" fill="#2b4a94"/>
  </svg>
  <div class="license">License: CSLB# 4871306</div>
</section>

</body>
</html>
```